Jewellery Store Web design

We are looking at a redesign of an exclusive jewellery store. The idea of what we want is to display the type of jewellery we sell. Our main product range is white diamonds. We do not want people to buy online. This site will not display any prices but only display photos and the information about the store.
The client believes in the saying “A picture makes a thousand words” so this site needs to be more pictures – less words.
The website that the client loves is:
www.morvelgems.com
The existing site can be found at:
http://www.brightwoodvault.com.au/
The site cannot be written in flash as the site must be viewable on iPad/iPhone devices and will be implemented with our already designed CMS.
This project is only for the PSD file. We will code up the final submission ourselves.
Updates
Reason: We have some great designs and we have decided to gurrantee the project and for those who want a payment gurrantee to enter.
Target Market(s)
Young Couples, 30+
Industry/Entity Type
Store
Look and feel
Each slider illustrates characteristics of the customer's brand and the style your logo design should communicate.

```html
<!DOCTYPE html>
<html lang="en">
<head>
<meta charset="utf-8">
<title>Brightwood – Home</title>
<link href="https://fonts.googleapis.com/css2?family=Jost:wght@400;500&display=swap" rel="stylesheet">
<style>
  :root {
    --header-top: #75787a;
    --header-mid: #3c3e40;
    --header-end: #0c0c0d;
    --header-rule: #141516;
    --nav-active: rgba(255,255,255,0.14);
    --text-light: #ffffff;
    --hair-light: #bfb39e;
    --hair-mid: #8f8270;
    --skin-light: #c9b2a6;
    --skin-mid: #8d7a72;
    --backdrop: #24272b;
    --band-dark: rgba(18,20,24,0.42);
    --welcome-panel: rgba(120,124,130,0.22);
  }
  * { margin: 0; padding: 0; box-sizing: border-box; }
  html, body { width: 1200px; height: 900px; overflow: hidden; background: var(--backdrop); }
  body { font-family: "Jost", "Futura", sans-serif; color: var(--text-light); }

  .page { position: relative; width: 1200px; height: 900px; overflow: hidden; }

  .hero-photo {
    position: absolute; left: 0; top: 140px; width: 1200px; height: 760px;
    background:
      radial-gradient(ellipse 520px 260px at 820px 140px, var(--hair-light) 0%, rgba(191,179,158,0.55) 45%, rgba(143,130,112,0) 100%),
      radial-gradient(ellipse 420px 300px at 1080px 330px, var(--hair-mid) 0%, rgba(143,130,112,0) 100%),
      radial-gradient(ellipse 260px 420px at 560px 470px, var(--skin-light) 0%, rgba(201,178,166,0.5) 50%, rgba(141,122,114,0) 100%),
      radial-gradient(ellipse 200px 260px at 300px 200px, var(--skin-mid) 0%, rgba(141,122,114,0) 100%),
      linear-gradient(90deg, var(--backdrop) 0%, #34363a 12%, #5a524d 40%, #6e6458 70%, #4a4641 100%);
  }

  .site-header {
    position: absolute; top: 0; left: 0; width: 1200px; height: 140px;
    background: linear-gradient(90deg, var(--header-top) 0%, var(--header-mid) 55%, var(--header-end) 100%);
    border-bottom: 8px solid var(--header-rule);
  }
  .main-nav { position: absolute; top: 65px; left: 0; width: 1200px; height: 64px; }
  .main-nav a {
    position: absolute; top: 0; height: 64px; line-height: 64px;
    transform: translateX(-50%);
    font-size: 34px; font-weight: 500; color: var(--text-light);
    text-decoration: none; text-shadow: 0 2px 4px rgba(0,0,0,0.7);
    white-space: nowrap;
  }
  .main-nav a.is-active { width: 143px; text-align: center; background: var(--nav-active); }

  .lower-band {
    position: absolute; left: 0; top: 653px; width: 1200px; height: 247px;
    background: var(--band-dark);
  }

  .welcome-panel {
    position: absolute; left: 75px; top: 357px; width: 630px; height: 296px;
    background: var(--welcome-panel); border-radius: 10px 10px 0 0;
  }
  .welcome-title {
    position: absolute; left: 153px; top: 372px;
    font-size: 95px; font-weight: 500; line-height: 84px; letter-spacing: -1px;
    white-space: nowrap;
  }
  .welcome-tagline {
    position: absolute; left: 160px; top: 540px;
    font-size: 34px; font-weight: 400;
  }

  .brand-name {
    position: absolute; left: 917px; top: 722px; transform: translateX(-50%);
    font-size: 66px; font-weight: 400; letter-spacing: 1px; white-space: nowrap;
    color: var(--text-light);
  }
</style>
</head>
<body>
<div class="page">
  <div class="hero-photo" role="img" aria-label="Close-up fashion portrait of a model with a sweeping blonde fringe across one eye, in soft muted tones"></div>

  <header class="site-header">
    <nav class="main-nav">
      <a class="is-active" href="#" style="left:104px">home</a>
      <a href="#" style="left:267px">About us</a>
      <a href="#" style="left:471px">Collection</a>
      <a href="#" style="left:695px">Diamonds</a>
      <a href="#" style="left:903px">Friends</a>
      <a href="#" style="left:1094px">Contact</a>
    </nav>
  </header>

  <div class="lower-band"></div>

  <div class="welcome-panel"></div>
  <h1 class="welcome-title">Welcome to<br>Brightwood</h1>
  <p class="welcome-tagline">the Luxury World</p>

  <div class="brand-name">BRIGHTWOOD</div>
</div>
</body>
</html>
```